Etiketten für Kuchen im Glas
Zielgruppe
Die Firma Brelkat bietet kulinarische Präsente und Geschenkideen zum Thema kreatives Backen an. Unsere Zielgruppe ist B2C und Werbetreibende, die unsere Produkte als Geschenke einsetzen.
Aufgabenstellung
Für unsere Zielgruppe "Feinkostläden" benötigen wir ein etwas edleres klasssisches Etiketten-Design.
Gestaltet wird der Deckel und die Vorderseite eines Etiketts für ein 290 ml FUMS-Glas. Die entsprechende Designvorlage steht hier zum Download bereit:
https://files.tralvex-speicher.de/u/4827351/7902_01358_0000-Vorlage%20CMYK%20v08_2013-09.psd
Benötigt werden 4 unterschiedliche Etiketten, die aber aus einem "Guss" sein sollten für die Sorten: Stracciatella, Schokolade, Zitrone, Stollen. Die Sorte sollte mit auf dem Etikett stehen.
Sonstige Angaben auf dem Etikett:
- optional "Kuchen im Glas"
- gerne Grünhof Logo (siehe Anhang)
- optional "fertig gebacken". Könnte z.B. gut auf dem Deckel in Kombination mit "Kuchen im Gla" stehen
Achtung: Das Etikett für die Rückseite mit Deklaration muss nicht gestaltet werden.
Tipps: Das Etikett ist konisch und das Glas rund. Das bedeutet, dass Bilder + Schriften mit einer leichten Wölbung kreiert werden sollten. Für die Wölbung kann man sich gut an der unteren Designlinie orientieren.
Farbgestaltung: eher dunkel; z.B. Grau, Dunkelblau evtl. Schwarz
Schriften: Es dürfen auch kostenpflichtige Schriften verwendet werden. Freie Schriften allerdings bevorzugt
Format: Photoshop PSD inklusive allen Ebenen und verwendeten Elementen als einzelne Ebene.
Bei Fragen gerne melden, ich freue mich auf Eure Designs.

```html
<!DOCTYPE html>
<html lang="de">
<head>
<meta charset="utf-8">
<title>Kuchen im Glas – Etiketten Schokolade</title>
<link href="https://fonts.googleapis.com/css2?family=Great+Vibes&family=Raleway:wght@400;600&display=swap" rel="stylesheet">
<style>
  :root {
    --page: #ffffff;
    --frame: #4a4a4a;
    --silver-light: #f4f4f4;
    --silver-mid: #c4c4c4;
    --silver-dark: #8a8a8a;
    --band: rgba(90, 90, 90, 0.28);
    --stitch: rgba(255, 255, 255, 0.85);
    --plaque-light: #ffffff;
    --plaque-shade: #e4e4e4;
    --plaque-edge: #5b3b2b;
    --navy: #1f2a63;
    --caption: #6d6d6d;
    --caption-light: #f5f5f5;
    --chocolate-light: #9a5a34;
    --chocolate-dark: #4a2512;
    --variety-fill: #f7f7f7;
    --variety-stroke: #5d5d5d;
    --eco-green: #2f9a3a;
    --eco-text: #2f2f2f;
  }
  html, body {
    margin: 0;
    padding: 0;
    overflow: hidden;
    background: var(--page);
  }
  .canvas {
    width: 1200px;
    height: 421px;
    box-sizing: border-box;
    border: 3px solid var(--frame);
    background: var(--page);
    position: relative;
    overflow: hidden;
  }
  .canvas svg {
    position: absolute;
    left: -3px;
    top: -3px;
    width: 1200px;
    height: 421px;
  }
  .tagline {
    font-family: "Raleway", sans-serif;
    font-size: 13px;
    letter-spacing: 0.6px;
    text-anchor: middle;
  }
  .tagline--on-silver { fill: var(--caption-light); }
  .tagline--on-plaque { fill: var(--caption); }
  .product-name {
    font-family: "Great Vibes", cursive;
    fill: var(--navy);
    text-anchor: middle;
    stroke: var(--navy);
    stroke-width: 0.6px;
  }
  .variety {
    font-family: "Great Vibes", cursive;
    fill: var(--variety-fill);
    stroke: var(--variety-stroke);
    stroke-width: 1.4px;
    paint-order: stroke;
    text-anchor: middle;
  }
  .eco-name {
    font-family: "Raleway", sans-serif;
    font-weight: 600;
    font-size: 15px;
    fill: var(--eco-text);
  }
</style>
</head>
<body>
<div class="canvas">
  <svg viewBox="0 0 1200 421" xmlns="http://www.w3.org/2000/svg">
    <defs>
      <radialGradient id="lid-silver" cx="50%" cy="45%" r="55%">
        <stop offset="0" stop-color="var(--silver-light)"/>
        <stop offset="0.6" stop-color="var(--silver-mid)"/>
        <stop offset="1" stop-color="var(--silver-dark)"/>
      </radialGradient>
      <linearGradient id="wrap-silver" x1="0" x2="1" y1="0" y2="0">
        <stop offset="0" stop-color="var(--silver-dark)"/>
        <stop offset="0.45" stop-color="var(--silver-light)"/>
        <stop offset="0.8" stop-color="var(--silver-mid)"/>
        <stop offset="1" stop-color="var(--silver-dark)"/>
      </linearGradient>
      <linearGradient id="plaque-fill" x1="0" x2="0" y1="0" y2="1">
        <stop offset="0" stop-color="var(--plaque-light)"/>
        <stop offset="1" stop-color="var(--plaque-shade)"/>
      </linearGradient>
      <linearGradient id="chocolate" x1="0" x2="1" y1="0" y2="1">
        <stop offset="0" stop-color="var(--chocolate-light)"/>
        <stop offset="1" stop-color="var(--chocolate-dark)"/>
      </linearGradient>
      <clipPath id="wrap-shape">
        <path d="M458 52 Q818 80 1180 52 L1158 385 Q818 430 480 385 Z"/>
      </clipPath>
    </defs>

    <!-- Deckel -->
    <g class="lid-label">
      <circle cx="190" cy="211" r="176" fill="url(#lid-silver)" stroke="var(--frame)" stroke-width="1"/>
      <rect role="img" aria-label="Silbernes Rautenmuster als Hintergrund" x="14" y="35" width="352" height="352" fill="none"/>
      <text class="tagline tagline--on-silver" x="190" y="78">- FERTIG GEBACKEN -</text>
      <path class="plaque"
            d="M83 100 H302 A20 20 0 0 0 322 120 V232 A20 20 0 0 0 302 252 H83 A20 20 0 0 0 63 232 V120 A20 20 0 0 0 83 100 Z"
            fill="url(#plaque-fill)" stroke="var(--plaque-edge)" stroke-width="5"/>
      <text class="product-name" x="192" y="200" font-size="48" textLength="222" lengthAdjust="spacingAndGlyphs">Kuchen im Glas</text>
      <rect role="img" aria-label="Schokoladenstücke" x="176" y="216" width="60" height="36" rx="3" fill="url(#chocolate)"/>
      <text class="variety" x="190" y="352" font-size="42">Schokolade</text>
    </g>

    <!-- Vorderseite, konisch -->
    <g class="wrap-label">
      <path d="M458 52 Q818 80 1180 52 L1158 385 Q818 430 480 385 Z"
            fill="url(#wrap-silver)" stroke="var(--frame)" stroke-width="1"
            role="img" aria-label="Silbernes Rautenmuster als Hintergrund"/>
      <g clip-path="url(#wrap-shape)">
        <path class="band" d="M440 150 Q818 192 1196 150 L1196 258 Q818 300 440 258 Z" fill="var(--band)"/>
        <path d="M440 158 Q818 200 1196 158" fill="none" stroke="var(--stitch)" stroke-width="1.5" stroke-dasharray="5 4"/>
        <path d="M440 250 Q818 292 1196 250" fill="none" stroke="var(--stitch)" stroke-width="1.5" stroke-dasharray="5 4"/>
      </g>
      <path class="plaque"
            d="M667 98 H890 A22 22 0 0 0 912 120 V238 A22 22 0 0 0 890 260 H667 A22 22 0 0 0 645 238 V120 A22 22 0 0 0 667 98 Z"
            fill="url(#plaque-fill)" stroke="var(--plaque-edge)" stroke-width="5"/>
      <text class="tagline tagline--on-plaque" x="778" y="130">- FERTIG GEBACKEN -</text>
      <text class="product-name" x="780" y="190" font-size="48" textLength="222" lengthAdjust="spacingAndGlyphs">Kuchen im Glas</text>
      <rect role="img" aria-label="Schokoladenstücke" x="772" y="212" width="66" height="38" rx="3" fill="url(#chocolate)"/>
      <path id="variety-arc" d="M690 318 Q780 330 870 318" fill="none"/>
      <text class="variety" font-size="38">
        <textPath href="#variety-arc" startOffset="50%">Schokolade</textPath>
      </text>
      <g class="eco-mark">
        <rect x="500" y="320" width="16" height="16" fill="var(--eco-green)"/>
        <text class="eco-name" x="521" y="333">Grünhof</text>
      </g>
    </g>
  </svg>
</div>
</body>
</html>
```